Business Card and Presentation Folder for Roofing Company
Business Card and Presentation Folder for Roofing Company - Construction
Creative Brief
Professional
Mark Ellis
Field Supervisor
2718 Brennan Ave Suite 310 Larkhaven, MO 63199
855-555-SEAL
mellis@slatepeak.example
www.SlatePeakRestoration.example
IL License #207.538142
stay with our colors of Yellow PMS 106, Black, and White
we want Logo Residential & Commercial 314-555-0178 Accredited Member of the QCA with an A+ Rating possible tag line: Everything you need under One Roof! or: Dedicated to being the most Trusted name in the Roofing Industry!
WendySlatePeak WendySlatePeak
COMBINE #217 AND #208 AND I WILL FINALIZE
#216...PLEASE MAKE THE CHANGES I REQUESTED SO I CAN FINALIZE THIS......
I extended the context
I uploaded an example of what I want our 2 presentation folders to look like: commercial folder: the 9 ICONS WILL BE: Flat roof Industrial building, Factory, City Highrise building, Apartment (3 story), Church, Gas Station, Restaurant, Hotel, & Bank Residential Folder: 9 ICONS WILL BE: House, House with flat roof, Condo, Siding, Gutters, Insulation, Ventilation, Storm Damage, Water&Fire Damage (together)
I uploaded our logos. Our colors are Yellow PMS106, Black, and White.....please use only these colors. Need business cards and Presentation Folder 9x12" (standard size) I will need the final files in Photoshop PSD file with all layers visible so I can make any future changes myself. Thanks Wendy

```html
<!DOCTYPE html>
<html lang="en">
<head>
<meta charset="utf-8">
<title>Slate Peak Restoration – Business Card and Presentation Folder</title>
<link href="https://fonts.googleapis.com/css2?family=Crimson+Pro:wght@400;600;700&display=swap" rel="stylesheet">
<style>
  :root {
    --yellow: #fedd00;
    --black: #111111;
    --white: #ffffff;
    --stage: #d6d6d6;
  }
  * { box-sizing: border-box; margin: 0; padding: 0; }
  html, body { width: 1200px; height: 1049px; overflow: hidden; }
  body {
    background: var(--stage);
    font-family: "Crimson Pro", "Times New Roman", serif;
    color: var(--black);
    position: relative;
  }

  .wordmark {
    font-weight: 700;
    text-transform: uppercase;
    color: var(--yellow);
    line-height: 1;
    letter-spacing: 0.04em;
    display: flex;
    align-items: center;
    gap: 10px;
  }
  .mark-square { background: var(--yellow); flex: none; display: block; }
  .wordmark-sub { display: block; letter-spacing: 0.12em; }

  /* ---------- Business card ---------- */
  .card {
    position: absolute;
    top: 30px;
    width: 540px;
    height: 300px;
    border-radius: 16px;
    overflow: hidden;
  }
  .card-front { left: 40px; background: var(--yellow); }
  .card-back { left: 620px; background: var(--black); }

  .holder { position: absolute; left: 36px; top: 100px; }
  .holder-name { font-size: 38px; font-weight: 400; line-height: 1.1; }
  .holder-title { font-size: 20px; margin-top: 2px; }

  .contact-list {
    position: absolute;
    left: 262px;
    top: 30px;
    list-style: none;
    font-size: 14px;
    line-height: 1.2;
  }
  .contact-list li { display: flex; align-items: flex-start; gap: 8px; margin-bottom: 6px; }
  .contact-list svg { width: 14px; height: 14px; flex: none; margin-top: 1px; }

  .front-band {
    position: absolute;
    left: 0; right: 0; bottom: 0;
    height: 40px;
    background: var(--black);
    display: flex;
    align-items: center;
    justify-content: space-between;
    padding: 0 26px 0 36px;
  }
  .license { color: var(--yellow); font-size: 14px; }
  .band-wordmark { font-size: 18px; }
  .band-wordmark .mark-square { width: 12px; height: 12px; }

  .back-wordmark {
    position: absolute;
    left: 0; right: 0; top: 42px;
    justify-content: center;
    font-size: 40px;
    text-align: center;
  }
  .back-wordmark .mark-square { width: 28px; height: 28px; }
  .back-wordmark .wordmark-sub { font-size: 26px; margin-top: 6px; }

  .back-band {
    position: absolute;
    left: 0; right: 0; top: 172px;
    height: 62px;
    background: var(--yellow);
    text-align: center;
    font-size: 18px;
    line-height: 1.25;
    padding-top: 8px;
  }
  .tagline {
    position: absolute;
    left: 0; right: 0; top: 252px;
    text-align: center;
    color: var(--yellow);
    font-size: 16px;
  }

  /* ---------- Presentation folder ---------- */
  .folder {
    position: absolute;
    top: 390px;
    width: 465px;
    height: 620px;
  }
  .folder-cover { left: 120px; background: var(--black); }
  .folder-inside {
    left: 615px;
    background: var(--white);
    box-shadow: inset 24px 0 30px -24px rgba(0,0,0,0.18);
    overflow: hidden;
  }

  .cover-wordmark {
    position: absolute;
    left: 0; right: 0; top: 110px;
    justify-content: center;
    font-size: 50px;
    text-align: center;
  }
  .cover-wordmark .mark-square { width: 34px; height: 34px; }
  .cover-wordmark .wordmark-sub { font-size: 32px; margin-top: 8px; }

  .cover-stripes { position: absolute; left: 0; right: 0; bottom: 34px; }
  .cover-stripes span { display: block; background: var(--yellow); }
  .cover-stripes .stripe-thick { height: 8px; }
  .cover-stripes .stripe-thin { height: 3px; margin-top: 5px; width: 72%; }

  .corner-wordmark {
    position: absolute;
    right: 20px; bottom: 8px;
    font-size: 16px;
    gap: 7px;
  }
  .corner-wordmark .mark-square { width: 10px; height: 10px; }

  .pocket {
    position: absolute;
    left: 0; right: 0; bottom: 0;
    height: 190px;
    background: var(--black);
  }
  .pocket-notch { position: absolute; left: 0; top: 0; display: block; }
</style>
</head>
<body>

  <section class="card card-front" aria-label="Business card front">
    <div class="holder">
      <p class="holder-name">Mark Ellis</p>
      <p class="holder-title">Field Supervisor</p>
    </div>
    <ul class="contact-list">
      <li><svg viewBox="0 0 14 14"><circle cx="7" cy="7" r="7" fill="#111"/><path d="M4.5 3.5l1.5 1.8-1 1a5 5 0 0 0 2.7 2.7l1-1 1.8 1.5-.9 1.2A6.5 6.5 0 0 1 3.3 4.4z" fill="#fedd00"/></svg>855-555-SEAL (Toll Free)</li>
      <li><svg viewBox="0 0 14 14"><circle cx="7" cy="7" r="7" fill="#111"/><path d="M4.5 3.5l1.5 1.8-1 1a5 5 0 0 0 2.7 2.7l1-1 1.8 1.5-.9 1.2A6.5 6.5 0 0 1 3.3 4.4z" fill="#fedd00"/></svg>314-555-0178</li>
      <li><svg viewBox="0 0 14 14"><circle cx="7" cy="7" r="7" fill="#111"/><path d="M4.5 3.5l1.5 1.8-1 1a5 5 0 0 0 2.7 2.7l1-1 1.8 1.5-.9 1.2A6.5 6.5 0 0 1 3.3 4.4z" fill="#fedd00"/></svg>314-555-0142</li>
      <li><svg viewBox="0 0 14 14"><circle cx="7" cy="7" r="7" fill="#111"/><path d="M4.5 3.5l1.5 1.8-1 1a5 5 0 0 0 2.7 2.7l1-1 1.8 1.5-.9 1.2A6.5 6.5 0 0 1 3.3 4.4z" fill="#fedd00"/></svg>314-555-0196</li>
      <li><svg viewBox="0 0 14 14"><circle cx="7" cy="7" r="7" fill="#111"/><rect x="3.5" y="4.5" width="7" height="5" fill="none" stroke="#fedd00"/><path d="M3.5 4.5L7 7.5l3.5-3" fill="none" stroke="#fedd00"/></svg>mellis@slatepeak.example</li>
      <li><svg viewBox="0 0 14 14"><circle cx="7" cy="7" r="7" fill="#111"/><circle cx="7" cy="7" r="3.6" fill="none" stroke="#fedd00"/><path d="M3.4 7h7.2M7 3.4v7.2" stroke="#fedd00"/></svg>www.SlatePeakRestoration.example</li>
      <li><svg viewBox="0 0 14 14"><circle cx="7" cy="7" r="7" fill="#111"/><path d="M7 11S4.2 7.8 4.2 6a2.8 2.8 0 0 1 5.6 0C9.8 7.8 7 11 7 11z" fill="#fedd00"/></svg><span>2718 Brennan Ave Suite 310 Larkhaven,<br>MO 63199</span></li>
    </ul>
    <div class="front-band">
      <span class="license">IL License #207.538142</span>
      <span class="wordmark band-wordmark"><span class="mark-square"></span>Slate Peak</span>
    </div>
  </section>

  <section class="card card-back" aria-label="Business card back">
    <div class="wordmark back-wordmark">
      <span class="mark-square"></span>
      <span>Slate Peak<span class="wordmark-sub">Restoration</span></span>
    </div>
    <div class="back-band">
      <p>Residential &amp; Commercial : 314-555-0178</p>
      <p>Accredited Member of the QCA with an A+ Rating</p>
    </div>
    <p class="tagline">Dedicated to being the most Trusted name in the Roofing Industry!</p>
  </section>

  <section class="folder folder-cover" aria-label="Presentation folder cover">
    <div class="wordmark cover-wordmark">
      <span class="mark-square"></span>
      <span>Slate Peak<span class="wordmark-sub">Restoration</span></span>
    </div>
    <div class="cover-stripes">
      <span class="stripe-thick"></span>
      <span class="stripe-thin"></span>
    </div>
    <div class="wordmark corner-wordmark"><span class="mark-square"></span>Slate Peak</div>
  </section>

  <section class="folder folder-inside" aria-label="Presentation folder inside pocket">
    <div class="pocket">
      <svg class="pocket-notch" width="465" height="14" viewBox="0 0 465 14" aria-hidden="true">
        <path d="M180 0Q196 0 204 10Q208 14 216 14H249Q257 14 261 10Q269 0 285 0z" fill="#fff"/>
      </svg>
    </div>
  </section>

</body>
</html>
```